Re-design of veterinary clinic website *

For a future relaunch of our webpage, we would like to find a fresh design that still incorporates the spirit of our current one which can be found at http://dr-wenzlaff.de
We are a small business that appeals to locals but are known in a wide area for specialist services.
According to analytics data, most people rarely read through the full website but are using it to inform themselves about opening hours, Telephone numbers and location. Still, the website needs to offer enough content to be ranked positively by the Quandle algorithm.
Our logo is not part of the re-design but needs to be included in your proposal as is. It can be used a source of inspiration, just as the current design. Keep in mind, that the design will be used as the basis of a fluid webdesign for both mobile and desktop. Roughly 75% of our users are on mobile devices.
Target Market(s)
Locals
Industry/Entity Type
Veterinary
Number of Pages Required
1 page
Look and feel
Each slider illustrates characteristics of the customer's brand and the style your logo design should communicate.

```html
<!DOCTYPE html>
<html lang="en">
<head>
<meta charset="utf-8">
<title>Dr. med. Konrad Wenzlaff – Small Animal Practice</title>
<link rel="stylesheet" href="https://fonts.googleapis.com/css2?family=Open+Sans:wght@400;600;700;800&display=swap">
<style>
:root{
  --blue:#253b86;
  --blue-dark:#132a74;
  --ink:#333333;
  --text:#3d3d3d;
  --hero-bg:#f1f1f1;
  --soft-bg:#f7f7f7;
  --white:#ffffff;
  --line:#e2e2e2;
  --rule:#c9c9c9;
}
*{box-sizing:border-box;margin:0;padding:0}
html,body{width:1200px;height:2594px;overflow:hidden;background:var(--white)}
body{font-family:"Open Sans",Arial,sans-serif;color:var(--text);position:relative}
.section{position:absolute;left:0;width:1200px}
.abs{position:absolute}

/* header */
.site-header{top:0;height:126px;background:var(--white)}
.brand{left:85px;top:40px;display:flex;align-items:center;gap:16px}
.brand-mark{width:34px;height:34px;border-radius:50%;background:var(--blue)}
.brand-name{font-size:30px;font-weight:700;color:var(--blue);letter-spacing:2px}

/* nav */
.main-nav{top:126px;height:45px;background:var(--blue)}
.nav-list{display:flex;list-style:none;margin-left:85px;height:45px}
.nav-list li{height:45px;display:flex;align-items:center;padding:0 23px;color:var(--white);font-size:15px;font-weight:700;letter-spacing:.5px}
.nav-list li.is-active{background:var(--blue-dark);padding:0 21px}

/* buttons */
.btn{display:flex;align-items:center;justify-content:center;background:var(--blue);color:var(--white);font-size:15px;font-weight:700;letter-spacing:1px;border-radius:3px;height:37px}

/* headings */
.section-title{left:0;width:1200px;text-align:center;color:var(--blue);font-size:33px;font-weight:700;letter-spacing:2.5px}
.title-rule{left:555px;width:90px;height:1px;background:var(--line)}
.body-copy{font-size:16px;line-height:19px;letter-spacing:.4px;color:var(--text)}
.body-copy p+p{margin-top:19px}

/* hero */
.hero{top:171px;height:486px;background:var(--hero-bg)}
.hero-photo{left:617px;top:30px;width:583px;height:456px;background:radial-gradient(ellipse at 55% 55%,#c59a6d 0%,#a97a4f 35%,#dcd2c6 75%,var(--hero-bg) 100%)}
.hero-text{left:83px;top:118px;width:520px;z-index:1}
.hero-kicker{font-size:33px;font-weight:700;color:var(--ink);letter-spacing:2px;line-height:40px}
.hero-name{font-size:28px;font-weight:700;color:var(--blue);letter-spacing:1.5px;line-height:38px;white-space:nowrap}
.hero-rule{left:85px;top:203px;width:88px;height:2px;background:var(--rule)}
.hero-intro{left:85px;top:218px;width:480px}
.hero-btn{left:85px;top:323px;width:152px}

/* about */
.about{top:657px;height:609px;background:var(--white)}
.about-copy{left:85px;top:173px;width:500px}
.about-btn{left:85px;top:463px;width:152px}
.about-photo{left:617px;top:178px;width:502px;height:339px;border:3px solid var(--blue);background:linear-gradient(160deg,#6b4a3a 0%,#8a6d4e 35%,#c7a98a 60%,#9b9a92 100%)}

/* office hours */
.hours{top:1266px;height:814px;background:var(--soft-bg)}
.hours-photo{left:85px;top:179px;width:505px;height:497px;background:radial-gradient(ellipse at 45% 55%,#9c8467 0%,#b9a58c 35%,#f3f1ee 75%,var(--white) 100%)}
.hours-copy{left:617px;top:173px;width:502px}
.hours-table{left:617px;top:428px;width:502px;border-collapse:collapse;font-size:15px}
.hours-table th{background:var(--blue);color:var(--white);font-weight:600;width:176px;height:39px;border:1px solid var(--white);letter-spacing:.5px}
.hours-table td{background:var(--white);width:178px;height:39px;text-align:center;border:1px solid var(--line);color:var(--text)}
.hours-table td:last-child{width:148px}
.hours-btn{left:794px;top:686px;width:150px}

/* services */
.services{top:2080px;height:470px;background:var(--white)}
.slider-arrows{left:1055px;top:107px;display:flex;gap:4px}
.slider-arrow{width:30px;height:28px;background:var(--soft-bg);display:flex;align-items:center;justify-content:center;border-radius:3px}
.service-tiles{left:85px;top:159px;display:flex;gap:26px}
.service-tile{width:239px;height:220px;display:flex;align-items:center;justify-content:center}
.tile-dogs{background:linear-gradient(180deg,#3b5196,#2b4189)}
.tile-dogs span{color:var(--white);font-size:20px;font-weight:700;letter-spacing:1.5px}
.tile-cats{background:linear-gradient(180deg,#5f6b3d,#7b6a52 55%,#4c3a2a)}
.tile-small{background:linear-gradient(180deg,#6c6a62,#b0764a 50%,#7e7466)}
.tile-young{background:linear-gradient(180deg,#5a5856,#8e8882 50%,#3a3937)}

/* footer */
.site-footer{top:2550px;height:44px;background:var(--blue);color:var(--white);font-size:15px;font-weight:700}
.copyright{left:85px;top:12px}
.imprint{right:81px;top:12px;letter-spacing:.5px}
</style>
</head>
<body>

<header class="section site-header">
  <div class="abs brand">
    <span class="brand-mark"></span>
    <span class="brand-name">Dr. med. vet. Konrad Wenzlaff</span>
  </div>
</header>

<nav class="section main-nav">
  <ul class="nav-list">
    <li class="is-active">HOME</li>
    <li>PRACTICE</li>
    <li>TEAM</li>
    <li>OFFICE HOURS</li>
    <li>SERVICES</li>
    <li>CONTACT US</li>
  </ul>
</nav>

<section class="section hero">
  <div class="abs hero-photo" role="img" aria-label="Group of pets: a large dog, a parrot, cats, kittens, a ferret and a tortoise"></div>
  <div class="abs hero-text">
    <h1 class="hero-kicker">WELCOME TO</h1>
    <div class="hero-name">DR. MED. KONRAD WENZLAFF</div>
  </div>
  <div class="abs hero-rule"></div>
  <p class="abs hero-intro body-copy">Welcome to the homepage of the veterinary practice of Dr. med. Konrad Wenzlaff. My team and I have put together information about the practice and information for patients.</p>
  <a class="abs btn hero-btn">READ MORE</a>
</section>

<section class="section about">
  <div class="abs title-rule" style="top:90px"></div>
  <h2 class="abs section-title" style="top:100px">ABOUT</h2>
  <div class="abs about-copy body-copy">
    <p>My small animal practice is located in the Lindenhofstrasse, which runs directly along the S - Bahn line S1, about 50 meters away from the S Bahnhof Birkenau.</p>
    <p>I founded the practice in 1985. The practice rooms were first in the Lindenhofstrasse 1. 1995 we moved into the current, larger rooms in the Lindenhofstrasse 2a.</p>
    <p>Among other things, the practice has 190 m2 of space, including two treatment rooms, an X-ray room, an operation preparation and recovery area and an operating room.</p>
    <p>The treatment rooms and the waiting room are air conditioned.</p>
  </div>
  <a class="abs btn about-btn">READ MORE</a>
  <div class="abs about-photo" role="img" aria-label="A dog and a cat lying together outdoors"></div>
</section>

<section class="section hours">
  <div class="abs title-rule" style="top:91px"></div>
  <h2 class="abs section-title" style="top:102px">OFFICE HOURS</h2>
  <div class="abs hours-photo" role="img" aria-label="A grey dog lying beside an alarm clock"></div>
  <div class="abs hours-copy body-copy">
    <p>From monday to saturday we are there for you during the following hours.</p>
    <p>In addition, you can arrange appointments outside of this time with us. This is particularly recommended for predictable examinations or treatments, such as vaccinations or dressings, more extensive examinations, detailed counseling sessions or even for particularly anxious or difficult to handle animals. Please let us know at the time of appointment on the phone with just how many animals you want to come and what we can do for you, so that we can take this into account in the scheduling.</p>
  </div>
  <table class="abs hours-table">
    <tr><th>MONDAY</th><td>9:30 - 11:00</td><td>16:00 - 19:00</td></tr>
    <tr><th>TUESDAY</th><td>9:30 - 11:00</td><td>16:00 - 19:00</td></tr>
    <tr><th>WEDNESDAY</th><td>9:30 - 11:00</td><td>16:00 - 19:00</td></tr>
    <tr><th>THURSDAY</th><td></td><td>16:00 - 19:00</td></tr>
    <tr><th>FRIDAY</th><td>9:30 - 11:00</td><td>16:00 - 19:00</td></tr>
    <tr><th>SATURDAY</th><td>9:30 - 11:00</td><td></td></tr>
  </table>
  <a class="abs btn hours-btn">READ MORE</a>
</section>

<section class="section services">
  <div class="abs title-rule" style="top:88px"></div>
  <h2 class="abs section-title" style="top:99px">OUR SERVICES</h2>
  <div class="abs slider-arrows">
    <span class="slider-arrow"><svg width="12" height="16" viewBox="0 0 12 16"><path d="M9 2 3 8l6 6" fill="none" stroke="#222" stroke-width="2"/></svg></span>
    <span class="slider-arrow"><svg width="12" height="16" viewBox="0 0 12 16"><path d="M3 2l6 6-6 6" fill="none" stroke="#222" stroke-width="2"/></svg></span>
  </div>
  <div class="abs service-tiles">
    <div class="service-tile tile-dogs" role="img" aria-label="White dog running, service: dogs"><span>DOGS</span></div>
    <div class="service-tile tile-cats" role="img" aria-label="Kittens in a wicker basket"></div>
    <div class="service-tile tile-small" role="img" aria-label="A young fox on a rock"></div>
    <div class="service-tile tile-young" role="img" aria-label="A grey puppy"></div>
  </div>
</section>

<footer class="section site-footer">
  <div class="abs copyright">Copyright © 2019 Dr. med. Konrad Wenzlaff</div>
  <div class="abs imprint">IMPRINT</div>
</footer>

</body>
</html>
```